LLC needs a business card design that emphasizes consulting and expert witness in upstream oil and g

I need a business card design for my company called Velmo Consultative Service, LLC. My expertise is in oil and gas upstream operations management to optimize performance and also as an expert witness for law firms in oil and gas upstream operations litigation.
The final design should communicate knowledge and hands-on experience as well as trust. (Velmo means rope or lasso. Perhaps "Velmo" should be in the form of a rope.) I do not like the color green in any shade. My first preference would be some shade of blue.

```html
<!DOCTYPE html>
<html lang="en">
<head>
<meta charset="utf-8">
<title>Velmo Consultative Service — Business Card</title>
<link rel="stylesheet" href="https://fonts.googleapis.com/css2?family=Tinos&display=swap">
<style>
  :root {
    --page: #eceae6;
    --card: #ffffff;
    --brand-blue: #2a4fae;
    --deep-blue: #1f3f9c;
    --sweep-blue: #2d56c4;
    --silver: #a9abb0;
    --contact: #ffffff;
  }
  * { margin: 0; padding: 0; box-sizing: border-box; }
  html, body {
    width: 1200px; height: 784px; overflow: hidden;
    background: var(--page);
    font-family: "Tinos", "Times New Roman", serif;
  }
  .sheet { position: relative; width: 1200px; height: 784px; }
  .card {
    position: absolute;
    width: 540px; height: 309px;
    background: var(--card);
    box-shadow: 0 6px 18px rgba(0,0,0,.18);
    overflow: hidden;
  }
  .card--front { left: 40px; top: 238px; }
  .card--back  { left: 620px; top: 238px; }
  .card__sweep { position: absolute; inset: 0; width: 100%; height: 100%; }
  .wordmark {
    position: absolute;
    display: flex; align-items: center; gap: 14px;
    color: var(--brand-blue);
  }
  .card--front .wordmark { left: 120px; top: 96px; }
  .card--back .wordmark  { left: 56px; top: 56px; }
  .wordmark__dot {
    width: 54px; height: 54px; border-radius: 50%;
    background: var(--brand-blue);
    flex: none;
  }
  .wordmark__text { display: flex; flex-direction: column; line-height: 1; }
  .wordmark__name { font-size: 58px; }
  .wordmark__tag  { font-size: 19px; margin-top: 4px; margin-left: 6px; }
  .contacts {
    position: absolute; left: 340px; top: 150px;
    list-style: none; color: var(--contact);
    font-size: 12.5px; line-height: 18px;
  }
  .contacts li { display: flex; align-items: flex-start; gap: 5px; white-space: nowrap; }
  .contacts svg { width: 13px; height: 13px; margin-top: 2px; flex: none; }
  .contacts .indent { padding-left: 18px; }
</style>
</head>
<body>
<main class="sheet">

  <section class="card card--front" aria-label="Card front">
    <div class="wordmark">
      <span class="wordmark__dot"></span>
      <span class="wordmark__text">
        <span class="wordmark__name">Velmo</span>
        <span class="wordmark__tag">Consultative Service</span>
      </span>
    </div>
  </section>

  <section class="card card--back" aria-label="Card back">
    <svg class="card__sweep" viewBox="0 0 540 309" preserveAspectRatio="none" aria-hidden="true">
      <defs>
        <linearGradient id="sweepFill" x1="0" y1="1" x2="1" y2="0">
          <stop offset="0" stop-color="#1f3f9c"/>
          <stop offset="1" stop-color="#2d56c4"/>
        </linearGradient>
        <linearGradient id="silverBand" x1="0" y1="0" x2="1" y2="0">
          <stop offset="0" stop-color="#e2e3e6"/>
          <stop offset="1" stop-color="#a9abb0"/>
        </linearGradient>
      </defs>
      <path d="M0 290 C180 240 330 90 540 -10 L540 2 C330 102 180 252 0 300 Z" fill="url(#silverBand)"/>
      <path d="M0 309 L0 306 C180 260 330 110 540 10 L540 309 Z" fill="url(#sweepFill)"/>
    </svg>

    <div class="wordmark">
      <span class="wordmark__dot"></span>
      <span class="wordmark__text">
        <span class="wordmark__name">Velmo</span>
        <span class="wordmark__tag">Consultative Service</span>
      </span>
    </div>

    <ul class="contacts">
      <li>
        <svg viewBox="0 0 16 16" aria-hidden="true"><path fill="#fff" d="M3 1.5l3 0 1 3.5-2 1.3a9 9 0 0 0 4.7 4.7L11 9l3.5 1v3c0 1-1 1.5-1.8 1.5C6.5 14 2 9.5 1.5 3.3 1.5 2.4 2 1.5 3 1.5z"/></svg>
        <span>555-201-4470</span>
      </li>
      <li>
        <svg viewBox="0 0 16 16" aria-hidden="true"><rect x="1" y="3" width="14" height="10" rx="1" fill="#fff"/><path d="M1.5 3.8 8 9l6.5-5.2" fill="none" stroke="#2d56c4" stroke-width="1.3"/></svg>
        <span>info@velmoconsultative.com</span>
      </li>
      <li>
        <svg viewBox="0 0 16 16" aria-hidden="true"><circle cx="8" cy="8" r="6.5" fill="none" stroke="#fff" stroke-width="1.4"/><path d="M1.5 8h13M8 1.5c-3 3.5-3 9.5 0 13M8 1.5c3 3.5 3 9.5 0 13" fill="none" stroke="#fff" stroke-width="1.1"/></svg>
        <span>www.velmoconsultative.com</span>
      </li>
      <li>
        <svg viewBox="0 0 16 16" aria-hidden="true"><path fill="#fff" d="M8 1.5 15 8h-2v6.5H9.5V10h-3v4.5H3V8H1z"/></svg>
        <span>4820 N. Prairie Road,</span>
      </li>
      <li class="indent"><span>Dallas, Texas 75201</span></li>
    </ul>
  </section>

</main>
</body>
</html>
```